Marketing Kit to include flyers and custom power point template

We need a fresh look for a marketing template to include custom flyers and a new power point template.
Updates

Flyers should be standard 8 1/2 x 11. We also need a custom power point template for presentations We are really looking for the design concept and will provide all the "text" after.

Target Market(s)

Businesses accepting credit cards

Industry/Entity Type

Marketing

Number of Pages Required

3 page

Requirements
Must have
• We need (2) Custom Flyers and one corresponding power point presentation template.
• Flyer 1 - "If we can't save you money we will pay you $1,000 guaranteed"
• Information to be added. We help you process your transactions correctly to save the most money with all card brands.
• - Needs a strong call to action
• Flyer 2 - Free EMV ready terminal. Are you able to accept the smart card?
• See attached flyer for some ideas. We want a matching design concept.
• for more info visit www.tallowgrid.com and www.morvenbay.com
Nice to have
• We want a powerful call to action with great pictures
Should not have
• lots of text

```html
<!DOCTYPE html>
<html lang="en">
<head>
<meta charset="utf-8">
<title>Larkfield Merchant Services – Flyers</title>
<link href="https://fonts.googleapis.com/css2?family=Roboto:wght@300;400;500;700&display=swap" rel="stylesheet">
<style>
  :root {
    --stage: #101112;
    --navy: #1a2c5a;
    --navy-deep: #0f2240;
    --stripe-blue: #1f4f7a;
    --green: #16a04a;
    --green-bright: #8bd13c;
    --cyan: #1fa8e6;
    --sky: #cfe4f4;
    --white: #ffffff;
    --header-top: #ffffff;
    --header-bottom: #d9dadc;
    --band-blue: #23336a;
    --band-violet: #352a78;
  }
  * { box-sizing: border-box; margin: 0; padding: 0; }
  html, body { width: 1200px; height: 1000px; overflow: hidden; }
  body {
    background: var(--stage);
    font-family: "Roboto", Arial, sans-serif;
    position: relative;
  }
  .flyer { position: absolute; height: 674px; overflow: hidden; background: #000; }
  .flyer--savings { left: 57px; top: 55px; width: 521px; }
  .flyer--emv { left: 624px; top: 268px; width: 522px; }
  .abs { position: absolute; }

  .header {
    left: 0; top: 0; width: 100%; height: 107px;
    background: linear-gradient(180deg, var(--header-top) 0%, var(--header-bottom) 100%);
  }
  .brand { display: flex; align-items: center; gap: 14px; }
  .brand__mark { width: 22px; height: 22px; background: var(--green); }
  .brand__text { display: flex; flex-direction: column; align-items: flex-end; }
  .brand__name {
    font-size: 42px; font-weight: 500; color: var(--navy); line-height: 1; letter-spacing: -0.5px;
  }
  .brand__tag { font-size: 15px; font-weight: 500; color: var(--green); margin-top: 4px; }

  .stripes {
    left: 0; width: 100%; height: 17px;
    background: linear-gradient(180deg,
      var(--navy-deep) 0 8px, var(--white) 8px 12px, var(--stripe-blue) 12px 17px);
  }
  .stripes--low {
    background: linear-gradient(180deg,
      var(--navy-deep) 0 7px, #000 7px 11px, var(--stripe-blue) 11px 17px);
  }

  .hero {
    left: 0; width: 100%;
    background:
      radial-gradient(ellipse at 62% 40%, #6d7480 0%, #2a2d33 30%, transparent 60%),
      linear-gradient(90deg, #050608 0%, #15171b 55%, #3a2418 100%);
  }
  .hero-text { color: var(--white); font-weight: 300; line-height: 1.0; white-space: nowrap; }
  .t-green { color: var(--green-bright); }
  .t-sky { color: var(--sky); }
  .t-cyan { color: var(--cyan); }

  .photo-row { left: 0; width: 100%; height: 122px; background: var(--white); }
  .photo { position: absolute; top: 0; height: 100%; }

  .band-green {
    left: 0; width: 100%;
    background: linear-gradient(90deg, #0d8b3c 0%, var(--green) 50%, #0e7c40 100%);
  }
  .band-blue {
    left: 0; width: 100%;
    background: linear-gradient(90deg, var(--band-blue) 0%, #1f3f78 45%, var(--band-violet) 100%);
  }
  .footer-strip {
    left: 0; width: 100%; height: 15px;
    background: linear-gradient(90deg, var(--green) 0%, #16495e 40%, var(--band-violet) 100%);
    color: var(--white); font-size: 10.5px; text-align: center; line-height: 15px; white-space: nowrap;
  }

  .contact { color: var(--white); font-size: 10.5px; line-height: 1.3; white-space: nowrap; }
  .contact strong { font-weight: 700; font-size: 11px; }
  .contact p + p { margin-top: 11px; }

  .pitch { color: var(--white); text-align: center; font-size: 14px; line-height: 1.5; }
  .pitch b { font-size: 16px; font-weight: 700; }
</style>
</head>
<body>

<!-- Flyer 1: savings guarantee -->
<section class="flyer flyer--savings">
  <header class="header abs">
    <div class="brand abs" style="left:32px; top:26px;">
      <span class="brand__mark"></span>
      <div class="brand__text">
        <span class="brand__name">Larkfield</span>
        <span class="brand__tag">merchant services</span>
      </div>
    </div>
  </header>
  <div class="stripes abs" style="top:107px;"></div>

  <div class="hero abs" role="img" aria-label="Hand in a dark suit holding out a chip credit card" style="top:124px; height:233px;"></div>
  <div class="hero-text abs" style="left:23px; top:154px; font-size:25px;">
    <div class="t-green">If We Can't Save</div>
    <div class="t-sky" style="margin-left:42px; margin-top:2px;">You Money</div>
  </div>
  <div class="hero-text abs" style="left:26px; top:266px;">
    <div class="t-cyan" style="font-size:27px;">We Will Pay You</div>
    <div style="font-size:46px; font-weight:700; margin-left:15px; margin-top:2px;">$1,000</div>
    <div style="font-size:19px; margin-left:85px; margin-top:-3px;">Guaranteed</div>
  </div>

  <div class="stripes stripes--low abs" style="top:357px;"></div>
  <div class="photo-row abs" style="top:376px;">
    <div class="photo" role="img" aria-label="Credit cards lying on banknotes" style="left:1px; width:172px; background:linear-gradient(135deg,#4a5a62,#a4a78a 60%,#3b4a66);"></div>
    <div class="photo" role="img" aria-label="Couple shopping online with a laptop on a sofa" style="left:176px; width:170px; background:linear-gradient(135deg,#e7e3da,#b69a7d 55%,#5f6f86);"></div>
    <div class="photo" role="img" aria-label="Group of business people in an office" style="left:349px; width:171px; background:linear-gradient(135deg,#d9dde0,#3c4048 55%,#8b7c72);"></div>
  </div>

  <div class="band-green abs" style="top:502px; height:70px;">
    <p class="pitch" style="margin-top:12px;">We help you <b>process</b> your <b>transactions</b> correctly to save the most<br><b>money with all card brands.</b></p>
  </div>
  <div class="band-blue abs" style="top:572px; height:86px;">
    <div class="contact abs" style="left:26px; top:20px;">
      <p><strong>Larkfield Merchant Services, Inc.</strong></p>
      <p>48 N Harbor St Suite 210<br>Riverton FL 32000</p>
    </div>
    <div class="contact abs" style="left:297px; top:12px;">
      <p>Our Primary number for agents and merchants<br><strong>(888) 555-0147 Toll Free</strong></p>
      <p>Our Primary fax for corporate communication<br><strong>(866) 555-0193</strong></p>
    </div>
  </div>
  <div class="footer-strip abs" style="top:658px;">Or email us at: info@larkfieldms.com&nbsp;&nbsp; Web: www.larkfieldms.com</div>
</section>

<!-- Flyer 2: EMV terminal -->
<section class="flyer flyer--emv">
  <header class="header abs">
    <div class="brand abs" style="left:34px; top:24px;">
      <span class="brand__mark"></span>
      <div class="brand__text">
        <span class="brand__name">Larkfield</span>
        <span class="brand__tag">merchant services</span>
      </div>
    </div>
  </header>
  <div class="stripes abs" style="top:107px;"></div>

  <div class="hero abs" role="img" aria-label="Hand in a dark suit holding out a chip credit card" style="top:124px; height:234px;"></div>
  <div class="hero-text abs" style="left:28px; top:136px; font-size:27px;">
    <div class="t-green" style="margin-left:18px;">Free EMV</div>
    <div class="t-sky">Ready terminal.</div>
  </div>
  <div class="hero-text abs" style="left:16px; top:266px;">
    <div class="t-cyan" style="font-size:26px; margin-left:53px;">Are you able</div>
    <div class="t-cyan" style="font-size:26px; margin-left:77px; margin-top:1px;">to Accept</div>
    <div class="t-cyan" style="font-size:31px; font-weight:700; margin-top:2px;">The Smart Card?</div>
  </div>

  <div class="stripes stripes--low abs" style="top:358px;"></div>
  <div class="photo-row abs" style="top:377px; height:123px;">
    <div class="photo" role="img" aria-label="Smartphone and bank cards on a laptop keyboard" style="left:1px; width:172px; background:linear-gradient(135deg,#5a6d86,#c6d3e0 50%,#2f3f5c);"></div>
    <div class="photo" role="img" aria-label="Shopper with bags at a store counter" style="left:176px; width:171px; background:linear-gradient(135deg,#8d2b34,#d7a4b4 50%,#6a5a4a);"></div>
    <div class="photo" role="img" aria-label="Cashier taking a card payment at a grocery till" style="left:350px; width:171px; background:linear-gradient(135deg,#c7b489,#f1ece2 50%,#6f8a4a);"></div>
  </div>

  <div class="band-green abs" style="top:502px; height:70px;"></div>
  <div class="band-blue abs" style="top:572px; height:88px;"></div>
  <div class="abs" role="img" aria-label="Faint rewards card with a gift bow" style="left:0; top:520px; width:226px; height:135px; background:linear-gradient(160deg,rgba(255,255,255,0.10),rgba(255,255,255,0.02));"></div>
  <div class="contact abs" style="left:297px; top:512px;">
    <p><strong>Larkfield Merchant Services, Inc.</strong></p>
    <p>48 N Harbor St Suite 210<br>Riverton FL 32000</p>
    <p style="margin-top:20px;">Our Primary number for agents and merchants<br><strong>(888) 555-0147 Toll Free</strong></p>
    <p>Our Primary fax for corporate communication<br><strong>(866) 555-0193</strong></p>
  </div>
  <div class="footer-strip abs" style="top:660px; height:14px; line-height:14px;">Or email us at: info@larkfieldms.com&nbsp;&nbsp; Web: www.larkfieldms.com</div>
</section>

</body>
</html>
```